Industrial Professional Business Card Design (Vantrel Systems)

Would like professional looking business cards. Not too busy leaning towards minimal. Should have a slogan like:
"Industrial Automation and Control".

We are a tech company that programs industrial PLC computers. We also develop custom hardware solutions. Please use the logo for inspiration.

Target Market(s)

Mining, industrial, processing, automation, factory

Industry/Entity Type

Engineering

Contact Information for Business Card

Name, phone, email, website. job title.

Font styles to use
Other font styles liked:
• droid sans

Requirements
Must have
• Use colours that go well with the logo. Not too busy design.

```html
<!DOCTYPE html>
<html lang="en">
<head>
<meta charset="utf-8">
<title>Vantrel Systems – Business Card</title>
<link href="https://fonts.googleapis.com/css2?family=Open+Sans:wght@400;600;700&display=swap" rel="stylesheet">
<style>
  :root {
    --page-bg: #e4e4e2;
    --card-bg: #2e2e2e;
    --card-edge: #f26a1b;
    --accent: #f26a1b;
    --brand-blue: #2a6db0;
    --text-light: #f2f2f2;
    --divider: #8a8a8a;
    --emboss-dark: #3a3a3a;
    --emboss-light: #686868;
  }
  * { box-sizing: border-box; margin: 0; padding: 0; }
  html, body {
    width: 1200px; height: 801px; overflow: hidden;
    background: var(--page-bg);
    font-family: "Open Sans", sans-serif;
  }
  .sheet {
    width: 1200px; height: 801px;
    display: flex; align-items: center; justify-content: center; gap: 60px;
  }
  .card {
    position: relative;
    width: 525px; height: 300px;
    background: var(--card-bg);
    border-bottom: 4px solid var(--card-edge);
    box-shadow: 0 10px 24px rgba(0,0,0,.25);
    overflow: hidden;
  }
  /* Front */
  .card-front__brand {
    position: absolute; left: 32px; top: 0; bottom: 0; width: 215px;
    display: flex; align-items: center; gap: 8px;
  }
  .brand-dot {
    width: 18px; height: 18px; border-radius: 50%;
    background: var(--accent); flex: none;
  }
  .brand-name {
    color: var(--brand-blue);
    font-weight: 600; font-size: 21px; letter-spacing: .2px; white-space: nowrap;
  }
  .card-front__divider {
    position: absolute; left: 268px; top: 70px; width: 1px; height: 160px;
    background: var(--divider);
  }
  .card-front__details {
    position: absolute; left: 292px; top: 68px; right: 20px;
    color: var(--text-light);
  }
  .person-name { color: var(--accent); font-weight: 700; font-size: 21px; line-height: 1.1; }
  .person-title { font-size: 15px; margin-top: 3px; }
  .address { font-size: 13px; line-height: 1.3; margin-top: 10px; }
  .contact-list { list-style: none; margin-top: 10px; font-size: 13px; line-height: 1.5; }
  .contact-list li { display: flex; align-items: center; gap: 8px; }
  .contact-list svg { width: 12px; height: 12px; flex: none; }
  .highlight { color: var(--accent); }
  /* Back */
  .card-back__emblem {
    position: absolute; left: -70px; bottom: -80px; width: 260px; height: 260px;
    border-radius: 50%;
    background: radial-gradient(circle at 60% 40%, var(--emboss-light), var(--emboss-dark) 75%);
  }
  .card-back__name {
    position: absolute; right: 30px; bottom: 70px;
    color: var(--text-light);
    font-weight: 600; font-size: 34px; letter-spacing: .4px; white-space: nowrap;
  }
</style>
</head>
<body>
<main class="sheet">
  <section class="card card-front">
    <div class="card-front__brand">
      <span class="brand-dot"></span>
      <span class="brand-name">Vantrel Systems</span>
    </div>
    <div class="card-front__divider"></div>
    <div class="card-front__details">
      <p class="person-name">Marcus Hale</p>
      <p class="person-title">Manager</p>
      <p class="address">Your address, city<br>state, ZIP 0000</p>
      <ul class="contact-list">
        <li>
          <svg viewBox="0 0 12 12"><path d="M3 1 L5 3 L4 4.5 Q5 7 7.5 8 L9 7 L11 9 L9.5 11 Q3 10 1 2.5 Z" fill="var(--accent)"/></svg>
          555-014-2100
        </li>
        <li>
          <svg viewBox="0 0 12 12"><rect x="1" y="2.5" width="10" height="7" fill="none" stroke="var(--accent)" stroke-width="1.3"/><path d="M1 2.5 L6 6.5 L11 2.5" fill="none" stroke="var(--accent)" stroke-width="1.3"/></svg>
          contact@vantrelmail.com
        </li>
        <li>
          <svg viewBox="0 0 12 12"><circle cx="6" cy="6" r="5" fill="none" stroke="var(--accent)" stroke-width="1.3"/><path d="M1 6 H11 M6 1 Q3 6 6 11 Q9 6 6 1" fill="none" stroke="var(--accent)" stroke-width="1"/></svg>
          <span>www.<span class="highlight">vantrelsystems</span>.com</span>
        </li>
      </ul>
    </div>
  </section>

  <section class="card card-back">
    <div class="card-back__emblem" role="img" aria-label="Large embossed brand emblem area"></div>
    <p class="card-back__name">Vantrel Systems</p>
  </section>
</main>
</body>
</html>
```